Business Card Design Project

New Business Card design for Varodine Technology Ltd using new Logo and new Tagline for staffing company.

About us from our website - www.varodine.example:

VaroDine is a leading and recognized Electronic Entertainment, Workforce Augmentation, and Project Management solutions provider with clients in Electronic Entertainment, Legal, Technology, Government and other verticals that range in size from start up organizations to Zenlar 500 companies. VaroDine is certified as an 8(a) minority and woman owned enterprise, established in 1998.

Target Market(s)

Companies in Electronic Entertainment, Legal, Government and Technology

Industry/Entity Type

Business

Requirements
Must have
• Must include in small letters the following information on back:

Established in 1998
8(a)(w)(e), Cage #7KRT9, DUNS #462137580

Front should have the following:
Derek Holloway
Vice President
5820 Birchmont Road
Fallowby, FB 482917
555-318-2746 X 100
555-902-6613 Fax
555-318-2746 Toll Free
name@varodine.example

Our Tagline: Connect • Collaborate • Achieve

```html
<!DOCTYPE html>
<html lang="en">
<head>
<meta charset="utf-8">
<title>VaroDine Business Card</title>
<link rel="stylesheet" href="https://fonts.googleapis.com/css2?family=Chakra+Petch:wght@500;700&family=Montserrat:wght@600;700&display=swap">
<style>
  :root {
    --stage: #000000;
    --brand-blue: #1560b5;
    --back-grey-light: #76797e;
    --back-grey-dark: #5d6065;
    --front-light: #f3f4f9;
    --front-tint: #e2e6f0;
    --ink-grey: #55585d;
    --ink-dark: #3c3f44;
    --white: #ffffff;
  }
  * { margin: 0; padding: 0; box-sizing: border-box; }
  html, body {
    width: 1200px; height: 644px; overflow: hidden;
    background: var(--stage);
  }
  .canvas { position: relative; width: 1200px; height: 644px; }
  .card {
    position: absolute; top: 168px;
    width: 540px; height: 308px; overflow: hidden;
  }
  .card--back { left: 40px; }
  .card--front { left: 620px; }

  .card__texture { position: absolute; inset: 0; }
  .card--back .card__texture {
    background: linear-gradient(135deg, var(--back-grey-light), var(--back-grey-dark));
  }
  .card--front .card__texture {
    background: radial-gradient(ellipse at 80% 30%, var(--front-light) 0%, var(--front-tint) 100%);
  }
  .card__corner { position: absolute; inset: 0; width: 540px; height: 308px; }

  .wordmark {
    position: absolute; display: flex; align-items: center; gap: 10px;
    font-family: "Montserrat", sans-serif; font-weight: 700; letter-spacing: -1px;
  }
  .wordmark__dot { border-radius: 50%; background: var(--brand-blue); }
  .card--back .wordmark {
    left: 50%; top: 152px; transform: translate(-50%, -50%);
    font-size: 62px; color: var(--white);
  }
  .card--back .wordmark__dot { width: 18px; height: 18px; }
  .card--front .wordmark {
    left: 162px; top: 142px; transform: translate(-50%, -50%);
    font-size: 36px; color: var(--ink-grey);
  }
  .card--front .wordmark__dot { width: 11px; height: 11px; }

  .credentials {
    position: absolute; left: 0; right: 0; top: 256px;
    text-align: center; color: var(--white);
    font-family: "Montserrat", sans-serif; font-weight: 600; text-transform: uppercase;
  }
  .credentials__since { font-size: 11px; letter-spacing: 0.5px; }
  .credentials__ids { font-size: 8.5px; margin-top: 2px; letter-spacing: 0.3px; }

  .contact {
    position: absolute; left: 282px; top: 76px;
    border-left: 1.5px solid var(--brand-blue);
    padding-left: 13px; height: 132px;
    font-family: "Chakra Petch", sans-serif; font-weight: 700;
    font-size: 10.5px; line-height: 12.5px; text-transform: uppercase;
    color: var(--ink-dark); letter-spacing: 0.4px;
  }
  .contact__group + .contact__group { margin-top: 11px; }
  .contact__label { color: var(--brand-blue); }

  .tagline {
    position: absolute; left: 0; right: 0; top: 264px; text-align: center;
    font-family: "Chakra Petch", sans-serif; font-weight: 700;
    font-size: 17px; font-variant: small-caps; letter-spacing: 0.6px;
    color: var(--brand-blue);
  }
</style>
</head>
<body>
<main class="canvas">

  <section class="card card--back" aria-label="Card back">
    <div class="card__texture" role="img" aria-label="Faint circuit-board line pattern on grey"></div>
    <svg class="card__corner" viewBox="0 0 540 308" aria-hidden="true">
      <polygon points="445,0 540,0 540,154" fill="var(--brand-blue)"/>
    </svg>
    <div class="wordmark"><span class="wordmark__dot"></span>VaroDine</div>
    <div class="credentials">
      <p class="credentials__since">Established in 1998</p>
      <p class="credentials__ids">8(a)(w)(e), Cage #7KRT9, DUNS #462137580</p>
    </div>
  </section>

  <section class="card card--front" aria-label="Card front">
    <div class="card__texture" role="img" aria-label="Faint circuit-board line pattern on pale blue-white"></div>
    <svg class="card__corner" viewBox="0 0 540 308" aria-hidden="true">
      <polygon points="0,0 142,0 0,154" fill="var(--brand-blue)"/>
    </svg>
    <div class="wordmark"><span class="wordmark__dot"></span>VaroDine</div>
    <div class="contact">
      <div class="contact__group">
        <p>VaroDine Elictric</p>
        <p>Title</p>
      </div>
      <div class="contact__group">
        <p>5820 Birchmont Road, Suite 340</p>
        <p>Fallowby, FB 482917</p>
      </div>
      <div class="contact__group">
        <p><span class="contact__label">Phone:</span> 555-318-2746 (X 100)</p>
        <p><span class="contact__label">Phone:</span> 1-800-555-0147 (Toll Free)</p>
        <p><span class="contact__label">Fax:</span> 555-902-6613 Fax</p>
        <p><span class="contact__label">Email:</span> name@varodine.example</p>
      </div>
    </div>
    <p class="tagline">Connect • Collaborate • Achieve</p>
  </section>

</main>
</body>
</html>
```